Design Brenvast.com Landing Page

Hello Freelancers!

this is an invitation to create our landing page (home) design. Brenvast is a Real Estate Investment Company and our Website is Private. That means that the only page available to public will be this one. The landing page should contain the description of the company and a Login Screen or button. Our expectation is to get a clean/classic/rich design with some real photoshop art skills.

This is what we will provide:

- Our Logo in PSD or ai
- Company Description

We need you to come up with a modern and rich design to represent our image. I have attached images of our Logo on different environment to inspire you. At this Point, we will need the PSD file that will be later on converted into a Joomla Web Page. The quality of the rendered logo on the different images provided is the type of quality design/image we would like. The attached file multimedia-world.jpg is a good example of quality work and imagination, it is not necessary a design for us but hopefully can be used as an reference.

Company Description;
Brenvast Capital Partners LLC (BCP) is a private real estate investment fund that invests in distressed real estate assets in Arizona, California, Florida, Michigan, Minnesota and Texas. The Fund focuses on existing properties and loans that are underperforming and undervalued.

Brenvast pursues smaller market single family real estate assets (less than $5 million) with its own capital and middle market assets ($1 to $10 million) along with its institutional investors. The Fund targets assets with significant value enhancement opportunities that can be captured in the near to mid-term. The Fund invests in quality pre-foreclosure, bankruptcy, foreclosure, and REO properties and loans that are operationally distressed.

Brenvast’s management has the market knowledge and real estate experience to take on complex transactions and formulate innovative investment solutions. The Fund deploys a variety of creative and flexible ownership structures and purchases fee simple interests, non-performing loans, and managing partner and similar positions.

Good Luck!

```html
<!DOCTYPE html>
<html lang="en">
<head>
<meta charset="utf-8">
<title>Brenvast Capital Partners</title>
<link rel="stylesheet" href="https://fonts.googleapis.com/css2?family=Cinzel:wght@400&family=Lato:wght@400;700&display=swap">
<style>
  :root {
    --indigo-deep: #23205f;
    --indigo: #3a3585;
    --indigo-light: #4c4799;
    --gold: #dfb21b;
    --gold-dark: #b88f0c;
    --navy: #16144f;
    --text: #ffffff;
    --muted: #cfcde6;
    --footer: #050508;
    --footer-text: #6d6d7a;
  }
  * { margin: 0; padding: 0; box-sizing: border-box; }
  html, body { width: 1200px; height: 869px; overflow: hidden; }
  body { font-family: "Lato", sans-serif; color: var(--text); position: relative; background: var(--indigo-deep); }

  .skyline-backdrop {
    position: absolute; inset: 0 0 42px 0;
    background:
      linear-gradient(180deg, rgba(42,38,110,0) 0%, rgba(42,38,110,0) 55%, rgba(30,27,85,.55) 100%),
      linear-gradient(180deg, #2f2b78 0%, #3c3789 45%, #443f92 62%, #2c2874 100%);
  }

  .brand-mark {
    position: absolute; left: 470px; top: 46px; width: 268px; height: 268px;
  }
  .brand-name {
    position: absolute; top: 318px; left: 0; width: 1200px; text-align: center;
    font-family: "Cinzel", serif; font-weight: 400; font-size: 44px; letter-spacing: 0.5px;
    color: var(--gold);
  }

  .login-form { position: absolute; left: 497px; top: 397px; width: 216px; }
  .field {
    display: flex; align-items: center; height: 32px; margin-bottom: 14px;
    background: var(--gold); border: 1px solid var(--gold-dark);
    padding-left: 10px; font-size: 14px; color: #4a3d10; letter-spacing: .5px;
  }
  .field svg { width: 16px; height: 16px; margin-right: 16px; fill: #3a2f0a; }
  .login-button {
    display: block; width: 216px; height: 30px; margin-top: 2px;
    background: var(--navy); color: var(--text); border: none;
    font-family: "Lato", sans-serif; font-size: 14px; letter-spacing: .5px;
  }
  .remember { margin-top: 30px; text-align: center; font-size: 12px; color: var(--muted); letter-spacing: .6px; }
  .remember .tick {
    display: inline-block; vertical-align: -3px; width: 15px; height: 15px; margin-right: 4px;
    background: var(--gold); border-radius: 2px;
  }
  .forgot { margin-top: 6px; text-align: center; font-size: 12px; color: var(--muted); letter-spacing: .6px; }

  .company-description {
    position: absolute; left: 215px; top: 610px; width: 773px;
    font-size: 12.6px; line-height: 17.3px; text-align: justify; color: var(--text);
  }
  .company-description p + p { margin-top: 17px; }

  .social-tabs { position: absolute; left: 0; top: 386px; }
  .social-tab {
    width: 29px; height: 41px; margin-bottom: 2px;
    background: var(--gold); border-radius: 0 6px 6px 0;
  }

  .site-footer {
    position: absolute; left: 0; bottom: 0; width: 1200px; height: 42px;
    background: var(--footer); color: var(--footer-text);
    font-size: 10px; text-align: center; line-height: 42px;
  }
</style>
</head>
<body>
  <div class="skyline-backdrop" role="img" aria-label="City skyline photograph across the waterfront, tinted deep indigo"></div>

  <svg class="brand-mark" viewBox="0 0 268 268" aria-hidden="true">
    <circle cx="134" cy="134" r="120" fill="none" stroke="var(--gold)" stroke-width="24"/>
  </svg>
  <h1 class="brand-name">Brenvast Capital Partners</h1>

  <form class="login-form">
    <div class="field">
      <svg viewBox="0 0 16 16"><circle cx="8" cy="4.5" r="3.8"/><path d="M1 16c0-4.5 3-7 7-7s7 2.5 7 7z"/></svg>
      User Name
    </div>
    <div class="field">
      <svg viewBox="0 0 16 16"><path d="M4.5 7V5a3.5 3.5 0 0 1 7 0v2h-1.8V5a1.7 1.7 0 0 0-3.4 0v2z"/><rect x="2.5" y="7" width="11" height="8.5" rx="1"/></svg>
      Password
    </div>
    <button type="button" class="login-button">LOGIN</button>
    <div class="remember">
      <svg class="tick" viewBox="0 0 15 15"><path d="M3 7.5l3 3 6-6.5" fill="none" stroke="#2a220a" stroke-width="2.2"/></svg>Remember me
    </div>
    <div class="forgot">Forgot Password?</div>
  </form>

  <section class="company-description">
    <p>Brenvast Capital Partners LLC (BCP) is a private real estate investment fund that invests in distressed real estate assets in Arizona, California, Florida, Michigan, Minnesota and Texas. The Fund focuses on existing properties and loans that are underperforming and undervalued.</p>
    <p>Brenvast pursues smaller market single family real estate assets (less than $5 million) with its own capital and middle market assets ($1 to $10 million) along with its institutional investors. The Fund targets assets with significant value enhancement opportunities that can be captured in the near to mid-term. The Fund invests in quality pre-foreclosure, bankruptcy, foreclosure, and REO properties and loans that are operationally distressed.</p>
    <p>Brenvast’s management has the market knowledge and real estate experience to take on complex transactions and formulate innovative investment solutions. The Fund deploys a variety of creative and flexible ownership structures and purchases fee simple interests, non-performing loans, and managing partner and similar positions.</p>
  </section>

  <nav class="social-tabs" aria-label="Social links">
    <div class="social-tab"></div>
    <div class="social-tab"></div>
    <div class="social-tab"></div>
    <div class="social-tab"></div>
  </nav>

  <footer class="site-footer">Copyright © 2010-2014 Brenvast Capital Partners LLC. All rights reserved.</footer>
</body>
</html>
```